Business card design needed

I am a Flower Essence/Light Therapist and am wanting a unique card that gives information. I am looking in particular for a card that folds and I would like the company name to be embossed if possible.
The information I need help on as it has to be short and concise but give the client information on what I do. My website is www.lanternmossgarden.com.au.
WHAT ARE FLOWER ESSENCES?
Flower essences are natural remedies that address negative emotional states, physical ailments, and can be taken when one wishes to develop a more positive mind-set and/or enhance one's wellbeing.

HOW DO I TAKE THEM?
Flower essences are usually ingested. They can be purchased as dilute (dosage) and concentrate (stock) strength bottles.
You can use the stock bottle itself - directions are usually written on the bottle.

Flower essences can (generally) also be used in the bath, spray bottles, added to gentle creams / oils or rubbed into the skin

Both dosage and stock strength bottles should be kept away from heat, light and radiation (e.g. computers, televisions, mobiles/cell phones).

If taken as directed, a dosage bottle course usually lasts about 2-4 weeks

HOW MUCH DO THEY COST? (inclusive of GST)
Initial Treatment (1.5hr) - $110
Includes Flower reading and personalised flower essence dosage.
Follow up visits - (30-45mins) - $75.00
Stress/Pain/Energy Management - $60.00
Meridian Healing for particular ailments - (30-45min) - $75.00
ie. anxiety, headaches, asthmas, fear etc
Light Therapy (Luvexa) - 30mins - $75.00

Reason: Still not happy with any designs

Target Market(s)

Trying to get the corporate market and everyone males and females but I think more for females and then they will talk to their husbands etc.

Industry/Entity Type

Business

Contact Information for Business Card

Lantern & Moss Garden

Requirements
Must have
• Must be folded so that people have information
Embossed
Unique not the norm
please visit www.lanternmossgarden.com.au

```html
<!DOCTYPE html>
<html lang="en">
<head>
<meta charset="utf-8">
<title>Lantern &amp; Moss Garden – Folded Card</title>
<link href="https://fonts.googleapis.com/css2?family=Questrial&family=Didact+Gothic&display=swap" rel="stylesheet">
<style>
  :root {
    --backdrop: #000000;
    --paper: #ffffff;
    --teal: #17a39c;
    --teal-deep: #0f8a84;
    --teal-light: #5cc4bd;
    --ink: #1a1a1a;
    --ink-soft: #333333;
  }
  * { margin: 0; padding: 0; box-sizing: border-box; }
  html, body { width: 1200px; height: 780px; overflow: hidden; background: var(--backdrop); }
  body { position: relative; font-family: "Questrial", "Didact Gothic", sans-serif; }

  .panel {
    position: absolute;
    background: var(--paper);
    border-radius: 22px;
    overflow: hidden;
  }
  .panel-bg { position: absolute; inset: 0; width: 100%; height: 100%; display: block; }
  .panel-content { position: absolute; inset: 0; }

  /* front spread */
  .panel--uses { left: 245px; top: 44px; width: 253px; height: 314px; }
  .panel--about { left: 500px; top: 44px; width: 512px; height: 314px; }
  /* back spread */
  .panel--prices { left: 245px; top: 410px; width: 510px; height: 315px; }
  .panel--contact { left: 757px; top: 410px; width: 255px; height: 315px; }

  .heading {
    position: absolute;
    font-size: 15px;
    line-height: 1.25;
    font-weight: 400;
  }
  .body-copy {
    position: absolute;
    font-family: "Didact Gothic", "Questrial", sans-serif;
    font-size: 10.2px;
    line-height: 1.32;
  }
  .on-paper { color: var(--ink); }
  .on-teal { color: var(--paper); }

  .uses-heading { left: 16px; top: 22px; width: 225px; }
  .uses-copy { left: 16px; top: 74px; width: 225px; }

  .brand-name {
    position: absolute;
    font-family: "Questrial", sans-serif;
    font-weight: 400;
    text-align: center;
    line-height: 1.15;
  }
  .uses-brand { left: 0; width: 253px; top: 250px; font-size: 19px; color: var(--paper); }

  .treat-heading { left: 18px; top: 14px; width: 240px; color: var(--paper); }
  .treat-copy { left: 18px; top: 40px; width: 228px; }
  .what-heading { left: 283px; top: 18px; width: 200px; color: var(--paper); }
  .what-copy {
    position: absolute; left: 283px; top: 70px; width: 215px;
    font-size: 15px; line-height: 1.3; color: var(--paper);
  }
  .happens-heading { left: 18px; top: 203px; width: 240px; }
  .happens-copy { left: 18px; top: 258px; width: 240px; }
  .site-url {
    position: absolute; left: 283px; top: 282px;
    font-size: 11.4px; color: var(--teal);
  }

  .price-list { position: absolute; left: 46px; top: 28px; width: 402px; list-style: none; }
  .price-item {
    font-family: "Didact Gothic", "Questrial", sans-serif;
    font-size: 10.6px; line-height: 1.45; color: var(--paper);
    margin-bottom: 15px;
  }
  .price-line { display: flex; align-items: baseline; }
  .price-leader { flex: 1; border-bottom: 1px dotted rgba(255,255,255,0.75); margin: 0 3px; transform: translateY(-3px); }
  .price-note { display: block; }
  .cost-title {
    position: absolute; right: 24px; top: 256px;
    font-size: 17px; font-weight: 700; color: var(--ink); font-family: "Didact Gothic", sans-serif;
    -webkit-text-stroke: 0.4px var(--ink);
  }
  .cost-sub {
    position: absolute; right: 24px; top: 282px;
    font-size: 13px; color: var(--ink); font-family: "Didact Gothic", sans-serif;
    -webkit-text-stroke: 0.3px var(--ink);
  }

  .contact-brand { left: 0; width: 255px; top: 68px; font-size: 24px; color: var(--teal); }
  .contact-rule { position: absolute; left: 20px; right: 20px; top: 96px; height: 1px; background: var(--teal-light); }
  .contact-details {
    position: absolute; left: 0; width: 255px; top: 210px;
    text-align: center; color: var(--paper); font-size: 21px; line-height: 1.3;
  }
</style>
</head>
<body>

  <!-- Front spread -->
  <section class="panel panel--uses">
    <svg class="panel-bg" viewBox="0 0 253 314" preserveAspectRatio="none" aria-hidden="true">
      <path d="M0,252 C70,246 150,196 253,198 L253,314 L0,314 Z" fill="var(--teal)"/>
    </svg>
    <div class="panel-content">
      <h2 class="heading uses-heading on-paper">What can Flower Essence Therapy be used for ?</h2>
      <p class="body-copy uses-copy on-paper">Flower essences can be used for releasing addictions or negative patterns, releasing trauma, Physical ailments, manifesting your desires, releasing fear and self-doubt, embracing the present moment and anything else that will bring you harmony. Essences are safe for adults, children and pets and work very gently to create subtle shifts over time.</p>
      <p class="brand-name uses-brand">Lantern &amp; Moss<br>Garden</p>
    </div>
  </section>

  <section class="panel panel--about">
    <svg class="panel-bg" viewBox="0 0 512 314" preserveAspectRatio="none" role="img" aria-label="Water droplet rippling on a teal surface">
      <defs>
        <radialGradient id="rippleFront" cx="0.62" cy="0.35" r="0.75">
          <stop offset="0" stop-color="var(--teal-light)"/>
          <stop offset="0.5" stop-color="var(--teal)"/>
          <stop offset="1" stop-color="var(--teal-deep)"/>
        </radialGradient>
      </defs>
      <rect width="512" height="314" fill="url(#rippleFront)"/>
      <path d="M0,204 C140,172 320,246 512,254 L512,314 L0,314 Z" fill="var(--paper)"/>
    </svg>
    <div class="panel-content">
      <h2 class="heading treat-heading">Flower Essence Treatments</h2>
      <p class="body-copy treat-copy on-teal">Your Flower Essence Therapy treatment begins with tuning into your specific needs and then identifying the flowers that will assist in balancing the mind and body. You'll leave with a custom flower essence blend that will support you and bring you into a greater state of balance.</p>
      <h2 class="heading what-heading">What is Flower Essence Therapy to ?</h2>
      <p class="what-copy">Flower Essence Therapy is the medicine of today. It covers different physical, emotional, mental and spiritual aspects, allowing us to wake up to our true reality.</p>
      <h2 class="heading happens-heading on-paper">What happens when I use flower essences ?</h2>
      <p class="body-copy happens-copy on-paper">As we use a flower essence, we begin to resonate in harmony with the qualities of the flower, and limitations begin to fade.</p>
      <p class="site-url">www.lanternmossgarden.com.au</p>
    </div>
  </section>

  <!-- Back spread -->
  <section class="panel panel--prices">
    <svg class="panel-bg" viewBox="0 0 510 315" preserveAspectRatio="none" role="img" aria-label="Water drops falling onto a rippling teal surface">
      <defs>
        <radialGradient id="rippleBack" cx="0.5" cy="0.45" r="0.7">
          <stop offset="0" stop-color="var(--teal-light)"/>
          <stop offset="0.55" stop-color="var(--teal)"/>
          <stop offset="1" stop-color="var(--teal-deep)"/>
        </radialGradient>
      </defs>
      <rect width="510" height="315" fill="url(#rippleBack)"/>
      <path d="M0,214 C110,300 330,300 510,208 L510,315 L0,315 Z" fill="var(--paper)"/>
    </svg>
    <div class="panel-content">
      <ul class="price-list">
        <li class="price-item">
          <span class="price-line"><span>Initial Treatment (1.5hr)</span><span class="price-leader"></span><span>$110</span></span>
          <span class="price-note">Includes Flower reading and</span>
          <span class="price-note">personalised flower essence dosage.</span>
        </li>
        <li class="price-item">
          <span class="price-line"><span>Follow up visits - (30-45mins)</span><span class="price-leader"></span><span>$75.00</span></span>
        </li>
        <li class="price-item">
          <span class="price-line"><span>Stress/Pain/Energy Treatment</span><span class="price-leader"></span><span>$60.00</span></span>
        </li>
        <li class="price-item">
          <span class="price-line"><span>Meridian Healing for particular ailments - (30-45min)</span><span class="price-leader"></span><span>$75.00</span></span>
          <span class="price-note">ie. anxiety, headaches, asthmas, fear etc</span>
        </li>
        <li class="price-item">
          <span class="price-line"><span>Light Therapy (Luvexa) - 30mins</span><span class="price-leader"></span><span>$75.00</span></span>
        </li>
      </ul>
      <h2 class="cost-title">How Much Do They Cost?</h2>
      <p class="cost-sub">(Inclusive Of Gst)</p>
    </div>
  </section>

  <section class="panel panel--contact">
    <svg class="panel-bg" viewBox="0 0 255 315" preserveAspectRatio="none" aria-hidden="true">
      <path d="M0,214 C70,198 160,190 255,188 L255,315 L0,315 Z" fill="var(--teal)"/>
    </svg>
    <div class="panel-content">
      <p class="brand-name contact-brand">Lantern &amp; Moss<br>Garden</p>
      <p class="contact-details">Marisol Avery<br>Phone 0491570156</p>
    </div>
  </section>

</body>
</html>
```